Successfully Managing through a Hurricane Training Event

This learning event is specifically for Birch Supply retailers/stores located outside of the US who are seeking guidance and help with how to plan, prepare, manage there business during Hurricane/Tropical Storm season.

----------------------------------------------
Event Title: Successfully Managing Through Hurricane Season

Event Description: Hurricanes and severe tropical storms are some of the most devastating, and costly, natural disasters known to humans. In fact, historically, 40% of small businesses impacted by a natural disaster do not reopen. If your business is vulnerable to these potential catastrophic events, it is important to develop an effective preparedness and mitigation plan, and take prompt action. Doing so will not only increase the safety of your store associates and customers, but it will help you remain in business after a hurricane strikes, improving your community’s ability to recover. This session focuses on:

o In-store preparation functions
o Implementing business continuity operating procedures for protecting and maintaining your business
o Sustaining the capability to provide products to customers
o Building a hurricane-ready optimized assortment of in-demand products, including special merchandising opportunities
o Deploying effective inventory management and system strategies for staying in stock
o Knowing your available contacts and rules of engagement
o Preserving a competitive advantage and reputation
o Optimizing the means by which you leverage your freight forwarding facility

Event is hosted by: Birch Worldwide Solutions www.birchworldservicesgroup.example

Logistical Details:
• Length: 1 hour
• Date: Friday, August 17, 2018
• Time: 1:00 – 2:00 p.m.

To Register for this Event, Go To: https://www.tovrelin.example/bir18/fall/

Pricing: $ 25 per participant
*Charged to Invoice post-show

Questions? For more information, contact Martin Olsby
+1 555-014-2836
molsby@birchsupply.example

Target Market(s)

Birch Supply International Stores

Industry/Entity Type

Retail

Font styles to use
Serif

Requirements
Must have
• See Word File Attachment
• Use Birch Supply red and black logo colors.
• 1 -Sided brochure
Nice to have
Should not have
• N/A

```html
<!DOCTYPE html>
<html lang="en">
<head>
<meta charset="utf-8">
<title>Successfully Managing Through Hurricane Season</title>
<link rel="stylesheet" href="https://fonts.googleapis.com/css2?family=Nunito+Sans:ital,wght@0,400;0,600;0,800;0,900;1,400&display=swap">
<style>
  :root {
    --red: #e31b37;
    --red-dark: #a9101f;
    --ink: #1b1b1b;
    --white: #ffffff;
    --backdrop: #ececec;
    --band: rgba(40, 44, 46, 0.72);
  }
  * { margin: 0; padding: 0; box-sizing: border-box; }
  html, body { width: 1200px; height: 1000px; overflow: hidden; }
  body {
    background: var(--backdrop);
    font-family: "Nunito Sans", Arial, sans-serif;
    color: var(--ink);
    position: relative;
  }
  .flyer {
    position: absolute; left: 233px; top: 12px;
    width: 749px; height: 968px;
    background: var(--white);
    overflow: hidden;
  }
  .brand {
    position: absolute; left: 30px; top: 46px;
    display: flex; align-items: center; gap: 12px;
  }
  .brand-dot { width: 46px; height: 46px; border-radius: 50%; background: var(--red); }
  .brand-name { font-size: 25px; font-weight: 800; color: var(--ink); letter-spacing: -0.3px; }
  .rule {
    position: absolute; left: 0; width: 100%;
    background: linear-gradient(90deg, var(--red-dark), var(--red) 30%, var(--red) 70%, var(--red-dark));
  }
  .rule-top { top: 98px; height: 10px; }
  .rule-mid { top: 528px; height: 8px; }
  .rule-bottom { top: 953px; height: 15px; }
  .hero-photo {
    position: absolute; left: 0; top: 108px; width: 100%; height: 420px;
    background: linear-gradient(180deg, #c9d3d6 0%, #9fb0b3 30%, #5e7270 55%, #3b4a48 80%, #2e3a39 100%);
  }
  .title-band {
    position: absolute; left: 0; top: 373px; width: 442px; height: 155px;
    background: var(--band);
  }
  .event-title {
    position: absolute; left: 29px; top: 395px;
    font-size: 33px; font-weight: 900; line-height: 41px;
    color: var(--white); text-transform: uppercase;
  }
  .date-box {
    position: absolute; left: 440px; top: 335px; width: 275px; height: 203px;
    background: var(--red); color: var(--white); text-align: center;
    box-shadow: 0 6px 14px rgba(0,0,0,0.25);
    padding-top: 60px;
  }
  .date-box .date { font-size: 27px; font-weight: 900; line-height: 32px; }
  .date-box .time { font-size: 34px; font-weight: 900; line-height: 38px; }
  .date-box .length { font-size: 14px; font-weight: 600; margin-top: 8px; }
  .info-panel {
    position: absolute; left: 447px; top: 538px; width: 268px; height: 397px;
    background: var(--red); color: var(--white); text-align: center;
  }
  .info-panel .label { font-size: 16px; font-weight: 900; line-height: 19px; text-transform: uppercase; }
  .register { position: absolute; top: 52px; width: 100%; }
  .register .url { font-size: 11px; font-weight: 600; text-decoration: underline; margin-top: 6px; text-transform: uppercase; letter-spacing: -0.1px; }
  .price { position: absolute; top: 132px; width: 100%; }
  .price .note { font-size: 11.5px; font-weight: 600; text-transform: uppercase; margin-top: 2px; }
  .contact {
    position: absolute; left: 17px; top: 187px; width: 234px; height: 131px;
    border: 1.5px solid var(--white); padding-top: 14px;
  }
  .contact .details { font-size: 12px; line-height: 15px; margin-top: 5px; text-transform: uppercase; }
  .host { position: absolute; top: 336px; width: 100%; }
  .host .label { font-size: 13px; line-height: 15px; }
  .host .url { font-size: 10.5px; font-weight: 600; margin-top: 5px; text-transform: uppercase; letter-spacing: -0.2px; white-space: nowrap; }
  .intro {
    position: absolute; left: 27px; top: 548px; width: 400px;
    font-size: 13.2px; font-style: italic; line-height: 16px;
  }
  .focus-heading {
    position: absolute; left: 27px; top: 698px;
    font-size: 15px; font-weight: 900; color: var(--red); text-transform: uppercase;
  }
  .focus-list { position: absolute; left: 34px; top: 723px; width: 380px; list-style: none; }
  .focus-list li {
    position: relative; padding-left: 25px;
    font-size: 12.4px; line-height: 13.5px; margin-bottom: 3px;
  }
  .focus-list svg { position: absolute; left: 0; top: 0; width: 15px; height: 15px; }
</style>
</head>
<body>
  <main class="flyer">
    <div class="brand">
      <span class="brand-dot"></span>
      <span class="brand-name">Birch Worldwide Solutions</span>
    </div>

    <div class="rule rule-top"></div>
    <div class="hero-photo" role="img" aria-label="Palm trees bending in hurricane winds beside a beach house, with surf spray"></div>
    <div class="title-band"></div>
    <h1 class="event-title">Successfully<br>Managing Through<br>Hurricane Season</h1>
    <div class="rule rule-mid"></div>

    <div class="info-panel">
      <div class="register">
        <p class="label">To Register for<br>this Event, Go To:</p>
        <p class="url">https://www.tovrelin.example/bir18/fall/</p>
      </div>
      <div class="price">
        <p class="label">$ 25 per Participant</p>
        <p class="note">*Charged to Invoice Post-Show</p>
      </div>
      <div class="contact">
        <p class="label">Questions?<br>For More Information,<br>Contact</p>
        <p class="details">Martin Olsby<br>+1 555-014-2836<br>molsby@birchsupply.example</p>
      </div>
      <div class="host">
        <p class="label">Event is Hosted By:<br>Birch Worldwide Solutions</p>
        <p class="url">www.birchworldservicesgroup.example</p>
      </div>
    </div>

    <div class="date-box">
      <p class="date">AUGUST 17, 2018</p>
      <p class="time">1:00 - 2:00 PM</p>
      <p class="length">LENGTH: 1 HOUR</p>
    </div>

    <p class="intro">Hurricanes and severe tropical storms are some of the most devastating, and costly, natural disasters known to humans. In fact, historically, 40% of small businesses impacted by a natural disaster do not reopen. If your business is vulnerable to these potential catastrophic events, it is important to develop an effective preparedness and mitigation plan, and take prompt action. Doing so will not only increase the safety of your store associates and customers, but it will help you remain in business after a hurricane strikes, improving your community’s ability to recover.</p>

    <h2 class="focus-heading">This Session Focuses On:</h2>
    <ul class="focus-list">
      <li><svg viewBox="0 0 16 16"><circle cx="7" cy="8.5" r="6" fill="none" stroke="#e31b37" stroke-width="1.3"/><path d="M4 8 L7 11 L14 2" fill="none" stroke="#e31b37" stroke-width="2"/></svg>In-store preparation functions</li>
      <li><svg viewBox="0 0 16 16"><circle cx="7" cy="8.5" r="6" fill="none" stroke="#e31b37" stroke-width="1.3"/><path d="M4 8 L7 11 L14 2" fill="none" stroke="#e31b37" stroke-width="2"/></svg>Implementing business continuity operating<br>procedures for protecting and maintaining your business</li>
      <li><svg viewBox="0 0 16 16"><circle cx="7" cy="8.5" r="6" fill="none" stroke="#e31b37" stroke-width="1.3"/><path d="M4 8 L7 11 L14 2" fill="none" stroke="#e31b37" stroke-width="2"/></svg>Sustaining the capability to provide products<br>to customers</li>
      <li><svg viewBox="0 0 16 16"><circle cx="7" cy="8.5" r="6" fill="none" stroke="#e31b37" stroke-width="1.3"/><path d="M4 8 L7 11 L14 2" fill="none" stroke="#e31b37" stroke-width="2"/></svg>Building a hurricane-ready optimized assortment<br>of in-demand products, including special<br>merchandising opportunities</li>
      <li><svg viewBox="0 0 16 16"><circle cx="7" cy="8.5" r="6" fill="none" stroke="#e31b37" stroke-width="1.3"/><path d="M4 8 L7 11 L14 2" fill="none" stroke="#e31b37" stroke-width="2"/></svg>Deploying effective inventory management and<br>system strategies for staying in stock</li>
      <li><svg viewBox="0 0 16 16"><circle cx="7" cy="8.5" r="6" fill="none" stroke="#e31b37" stroke-width="1.3"/><path d="M4 8 L7 11 L14 2" fill="none" stroke="#e31b37" stroke-width="2"/></svg>Knowing your available contacts and rules of engagement</li>
      <li><svg viewBox="0 0 16 16"><circle cx="7" cy="8.5" r="6" fill="none" stroke="#e31b37" stroke-width="1.3"/><path d="M4 8 L7 11 L14 2" fill="none" stroke="#e31b37" stroke-width="2"/></svg>Preserving a competitive advantage and reputation</li>
      <li><svg viewBox="0 0 16 16"><circle cx="7" cy="8.5" r="6" fill="none" stroke="#e31b37" stroke-width="1.3"/><path d="M4 8 L7 11 L14 2" fill="none" stroke="#e31b37" stroke-width="2"/></svg>Optimizing the means by which you leverage your<br>freight forwarding facility</li>
    </ul>

    <div class="rule rule-bottom"></div>
  </main>
</body>
</html>
```